Design of Premium Instant Tea Packaging (Tea in 3 seconds)

We need a fully packaging and sachets design for our new premium instant tea (Tea in 3 seconds) collection to our new brand BrimLeaf. The company is based in Norway and are founded by two Norwegian with a passion for tea and with a mission to share our passion in a faster and easier manner.

We would like a design that gives an exclusive, healthy, tasty and warm feeling. The design should communicate instant tea of high quality.

The tea is one of the first premium instant tea on the market and should give the customer a feeling of exclusive innovation, A new tea company is in town. We don't want to be similar to other old granny tea companies and we hate tea bags :P.

About our products. We offer two different Flavours:
Brim Hibiscus and Brim Lemon. The Brim Hibiscus is sweet and red as blood in its color.

We are looking for a universal design where we can change the color and text based on the flavors. So is important that we get the edible design for front and back of the packages and sachets. Each package contains 10 small sachets where the design of the sachets should be a similar design as the packages itself.

I will provide an example picture/template (just a guideline, not obligatory) from the factory and the sachets, but also from our competitors. Is important that both packaging design and sachets design is editable from both sides if we in the future add new flavors or text.

I will also provide a word file with the necessary text on the pack of the packaging and Nutrition Facts for both of the two flavors. Important that the ingredients are a least in both Norwegian (N) and English (GB). The word file also contains the company information, put on the back of the packaging.

Attached pls find two pictures of design template. Maybe you need them when designing. It's the dimension of 10 sachets/box and 0.6g/sachet the factory use. Our logo BrimLeaf should be on the packaging and the sachets. I also provided the logo in editable format.

Brim Instant Lemon:
GB Ingredients : Lemon, black tea
N Ingredienser: Sitron, svart te

Brim Instant Hibiscus:
GB Ingredients: Hibiscus, rose, black tea and stevia extract
N Ingredienser: Hibiscus, rose, svart te og stevia ekstrakt

Experience the new generation of tea! BrimLeaf® is one of the world fist premium instant tea. Made from real fruit and whole tea leaf, you get incredible tea in seconds. Based on patented cold-brewed technology provide you with the essence of tea, without the need for sugar or preservatives. Brim with health, Brim with taste!

Distributed by Korvenet AS®
PO BOX: 4027
Oslo, Mørkedalsgata 5, Norway
Learn more at BrimLeaf.example

Hope your design can help us stand out from the crowd.

With best regards,

Torvald
CEO of Korvenet As

Target Market(s)

The beverages market, or more correctly the tea market.
The product is Premium Instant Tea.

Font styles to use
Serif

Colors

Designer to choose colors to be used in the design.

Requirements
Must have
• The name of the tea flavor in its representative color.
• Brim Instant Lemon
• Premium Black tea (Smaller letters)
• Brim Instant Hibiscus
• Premium Herbal Tea (Smaller letters)
• General facts:
• * 100 % Natural, no additives, artificial flavors or preventative.
• * 0 fat/ 0 Sugar / 0 Calories.
• * In Crystal instead of tea powder or tea bag.
• * It is soluble in 3 seconds with 200 ml to 300 ml hot or cold pure water.
• Looking for a design where we can change the color and text based on the different flavors. So is important that we get the edible design for the and back of the packages and sachets.
• Ingredients in Norwegian (N) and English(GB) and nutrition values in Norwegian and if possible in English. Remember the company information (provided in the packeging.docx) at the back with a link to our website, www.BrimLeaf.example.
• Must show how the product works on the front and the back. Remember instant tea in 3 seconds from sachets. 10 sachets in each pack, should be a part of the front information, see provided examples.
• Important that we can easily change it our self with affinity or other programs, based on new text or flavor. So we need 360-degree design, so we can change the back and the front, based on what our factory can print out.
• Remember that the design should be reused many times, not just for one of those two flavors above. Simple, but yet elegant and upmarket.
• Each package contains 10 small sachets where the design of the sachets should be a similar design as the packages itself. I will provide an example picture/template from the factory and the sachets, but also from our competitors.
• Is important that both packaging design and sachets design is editable from both sides if we in the future add new flavors or text. I will also provide a word file with the necessary text on the pack of the packaging and Nutrition Facts for both of the two flavors. Important that the ingredients are a least in both Norwegian (N) and English (GB). The word file also contains the company information, put on the back of the packaging.
• Brim Lemon:
• GB Ingredients: Lemon, black tea
• N Ingredienser: Sitron, svart te
• Brim Hibiscus:
• GB Ingredients: Hibiscus, rose, black tea and stevia extract
• N Ingredienser: Hibiscus, rose, svart te og stevia ekstrakt
• Text on the back:
• Experience the new generation of tea! BrimLeaf® is one of the world fist premium instant tea. Made from real fruit and whole tea leaf, you get incredible tea in seconds. Based on patented cold-brewed technology provide you with the essence of tea, without the need for sugar or preservatives. Brim with health, Brim with taste!
• Company information:
• Distributed by Korvenet AS®
• PO BOX: 4027
• Oslo, Mørkedalsgata 5, Norway
• Learn more at www.BrimLeaf.example
Nice to have
• Take a look at Bemo Tea, Vardy Tea and Hollet.
• Especially Hollet since they have a clean and high-class design. https://www.holletleaf.example/tea-by-type/indian-breakfast-25-tea-bags?___SID=U.
• Nice with ® on top of the A on BrimLeaf logo.
• Quiro has also nice designs: https://www.quiroleaf.example/us/en/products/hot.html
• Remember the sticking out / eye-catcher". For both of these proposals, I think that if it had some gold elements in the same way that Sundmark coffee has (a little more expensive for flavor) and that the white color of the proposal one is replaced by light black on the sides and either black or gold in the field where the text. In other words, I think that the packaging should be as identical as possible regardless of taste.
• Feedback for Manufacturer: (Just suggestion from her)
• About the packaging, my suggestion is as follows:
• 1) I think color should match "lemon black tea".We'd better choose the color which in coordination with the flavor, for customer's observation conveniently.
• 2) As for the phrase "cold water instant tea", I think it'd better we remark "stir or shake for better dissolving" or similar meanings in the package. Or describing it by pattern as the attachment FYI. Because these two flavors contain black tea which has enzyme. The molecule of enzyme is a little bigger, so it's a little hard to be totally dissolved by cold water without stirring or shaking.
• Pure tea in hot or cold pure water for you anytime, everywhere on the go (On the back
Should not have
• We hate Parvel, Ashcombe's design. Remember simple, modern and elegant. We are the future of tea, don't make your grandma happy with the design!
• Please avoid using teacups in the design!
• Best regards,
• Torvald

```html
<!DOCTYPE html>
<html lang="en">
<head>
<meta charset="utf-8">
<title>BrimLeaf – Brim Hibiscus Redtea Sachet</title>
<link rel="stylesheet" href="https://fonts.googleapis.com/css2?family=Cinzel:wght@600&family=Tinos&display=swap">
<style>
  :root {
    --page: #f6f6f6;
    --paper: #ffffff;
    --ink: #2a2a2a;
    --ink-soft: #7a7a7a;
    --rule: #9a9a9a;
    --hibiscus: #d8281e;
    --hibiscus-deep: #a8140f;
    --hibiscus-light: #e5463a;
    --leaf: #47683a;
    --corner: #1f2733;
    --icon-tone: #bdbdbd;
  }
  * { box-sizing: border-box; margin: 0; padding: 0; }
  html, body { width: 1200px; height: 1200px; overflow: hidden; }
  body { background: var(--page); position: relative; font-family: "Tinos", serif; color: var(--ink); }

  .sachet-front {
    position: absolute; top: 122px; width: 210px; height: 932px;
    background: var(--paper); border-radius: 16px; overflow: hidden;
    box-shadow: 2px 0 6px rgba(0,0,0,0.06);
  }
  .sachet-front--a { left: 98px; }
  .sachet-front--b { left: 376px; }

  .flower-column {
    position: absolute;
    background:
      linear-gradient(90deg, rgba(71,104,58,0.35) 0%, rgba(71,104,58,0) 22%, rgba(71,104,58,0) 78%, rgba(71,104,58,0.3) 100%),
      linear-gradient(180deg,
        var(--hibiscus) 0%, var(--hibiscus-deep) 12%, var(--hibiscus-light) 22%,
        var(--hibiscus-deep) 34%, var(--hibiscus) 46%, var(--hibiscus-deep) 58%,
        var(--hibiscus-light) 70%, var(--hibiscus-deep) 82%, var(--hibiscus) 100%);
  }
  .sachet-front .flower-column { left: 10px; right: 20px; top: 6px; bottom: 6px; border-radius: 60px; }

  .label-panel {
    position: absolute; background: var(--paper); border: 1px solid #c9c9c9;
    text-align: center; display: flex; flex-direction: column; align-items: center; justify-content: center;
  }
  .sachet-front .label-panel { left: 0; width: 194px; top: 358px; height: 228px; }

  .brand-mark { display: flex; align-items: center; gap: 8px; margin-bottom: 4px; }
  .brand-mark .dot { width: 9px; height: 9px; border-radius: 50%; background: var(--ink-soft); }
  .brand-name { font-family: "Cinzel", serif; font-weight: 600; font-size: 22px; letter-spacing: 1px; color: var(--ink); }
  .brand-rule { width: 130px; height: 1px; background: var(--rule); margin: 8px 0 22px; }
  .product-name { font-size: 19px; line-height: 1.15; letter-spacing: 0.3px; color: var(--ink); }
  .product-type { font-size: 12px; color: var(--ink-soft); margin-top: 6px; }

  .sachet-flat {
    position: absolute; left: 646px; top: 122px; width: 460px; height: 928px;
    background: var(--paper); border: 1px solid var(--ink);
  }
  .corner { position: absolute; width: 45px; height: 36px; background: var(--corner); }
  .corner--tl { left: 0; top: 0; } .corner--tr { right: 0; top: 0; }
  .corner--bl { left: 0; bottom: 0; } .corner--br { right: 0; bottom: 0; }
  .sachet-flat .flower-column { left: 144px; width: 176px; top: 0; bottom: 0; border-radius: 60px; }
  .sachet-flat .label-panel { left: 140px; width: 190px; top: 368px; height: 192px; }
  .sachet-flat .brand-name { font-size: 20px; }
  .sachet-flat .brand-rule { margin-bottom: 16px; }
  .sachet-flat .product-name { font-size: 17px; }
  .sachet-flat .product-type { font-size: 11px; }

  .rotated {
    position: absolute; white-space: nowrap; transform: translate(-50%, -50%) rotate(-90deg);
    font-size: 14px; line-height: 19px;
  }
  .company-info { left: 92px; top: 464px; }
  .net-weight { left: 372px; top: 468px; text-align: center; }

  .steps { position: absolute; left: 344px; width: 46px; }
  .steps--bottle { top: 256px; height: 126px; }
  .steps--stir { top: 556px; height: 110px; }
  .step-art {
    position: absolute; left: 0; top: 0; width: 34px; height: 100%; border-radius: 10px;
    background: linear-gradient(180deg, rgba(189,189,189,0.25), var(--icon-tone) 50%, rgba(189,189,189,0.25));
  }
  .step-num { position: absolute; left: 38px; font-size: 10px; transform: rotate(-90deg); }
  .steps--bottle .n1 { top: 112px; } .steps--bottle .n2 { top: 62px; } .steps--bottle .n3 { top: 12px; }
  .steps--stir .n1 { top: 96px; } .steps--stir .n2 { top: 56px; } .steps--stir .n3 { top: 16px; }
</style>
</head>
<body>

  <div class="sachet-front sachet-front--a">
    <div class="flower-column" role="img" aria-label="Column of red hibiscus flowers with green leaves"></div>
    <div class="label-panel">
      <div class="brand-mark"><span class="dot"></span><span class="brand-name">BrimLeaf</span></div>
      <div class="brand-rule"></div>
      <div class="product-name">BRIM HIBISCUS<br>REDTEA</div>
      <div class="product-type">Premium Instant Herbal Tea</div>
    </div>
  </div>

  <div class="sachet-front sachet-front--b">
    <div class="flower-column" role="img" aria-label="Column of red hibiscus flowers with green leaves"></div>
    <div class="label-panel">
      <div class="brand-mark"><span class="dot"></span><span class="brand-name">BrimLeaf</span></div>
      <div class="brand-rule"></div>
      <div class="product-name">BRIM HIBISCUS<br>REDTEA</div>
      <div class="product-type">Premium Instant Herbal Tea</div>
    </div>
  </div>

  <div class="sachet-flat">
    <span class="corner corner--tl"></span><span class="corner corner--tr"></span>
    <span class="corner corner--bl"></span><span class="corner corner--br"></span>

    <div class="flower-column" role="img" aria-label="Column of red hibiscus flowers with green leaves"></div>

    <div class="rotated company-info">
      Distributed by&nbsp; Korvenet AS® PO BOX: 4027<br>
      Oslo, Mørkedalsgata 5, Norway<br>
      Learn more at BrimLeaf.example
    </div>

    <div class="label-panel">
      <div class="brand-mark"><span class="dot"></span><span class="brand-name">BrimLeaf</span></div>
      <div class="brand-rule"></div>
      <div class="product-name">BRIM HIBISCUS<br>REDTEA</div>
      <div class="product-type">Premium Instant Herbal Tea</div>
    </div>

    <div class="steps steps--bottle">
      <div class="step-art" role="img" aria-label="Three-step pictograms: pour crystals into a bottle, shake, ready to drink"></div>
      <span class="step-num n1">1.</span><span class="step-num n2">2.</span><span class="step-num n3">3.</span>
    </div>

    <div class="rotated net-weight">NET WET 0.6 g<br>(0.02 OZ)</div>

    <div class="steps steps--stir">
      <div class="step-art" role="img" aria-label="Three-step pictograms: tear sachet, pour into water, stir"></div>
      <span class="step-num n1">1.</span><span class="step-num n2">2.</span><span class="step-num n3">3.</span>
    </div>
  </div>

</body>
</html>
```